Design Health Food E-Book for Small Business Using Provided Content

My business is looking for a designer to design and create an e-book PDF with recipes and images.

The required work will be:

Designing layout of e-book based on provided (below) e-book sample.

Adding supplied recipes and images into a PDF format

Iterating PDF until the work has reached satisfactory requirements

The outcome will be:

1 PDF document (roughly 10-15 pages) created using supplied recipes and images

This recipe e-book by Delia Marsh should serve as a strong piece of inspiration.

https://stirgrowthrive.shopvane.example/item/83k27dq4m190xz55t6b3c8e1

The full content of the e-book, including photos and copy, can be found here:

https://www.filecrate.example/sh/qrt517xk29w304b/BBDkunhwUPoeTvMzq8ErTXf4Gb?dl=0

Please arrange for a skype conversation if further clarification of e-book output and/or design are necessary.

Email: tobyr839@postmix.example

Industry/Entity Type

Health And Wellness

Font styles to use
Other font styles liked:
• Designer Choice

Requirements
Must have
• Book-like appearance (as in actually looks like a recipe book as opposed to a flyer, photo collection etc.
• Flawless page-linking (from contents page and to external sources) and no errors in text (unless we put a typo in!)
• Cute extra graphics (as per supplied Delia Marsh book)
Nice to have
• Designer interested in health food
• Experience in e-book design
Should not have
• Typos
• Errors in text linking

```html
<!DOCTYPE html>
<html lang="en">
<head>
<meta charset="utf-8">
<title>Morning Mission – Tuesday: Epic Toast Toppers</title>
<link rel="stylesheet" href="https://fonts.googleapis.com/css2?family=Itim&family=Sniglet:wght@400;800&display=swap">
<style>
  :root {
    --paper: #ffffff;
    --rust: #c0581e;
    --cocoa: #5a2812;
    --ink: #5b2611;
    --slate: #1c2231;
    --sketch-bg: #f6f1ec;
  }
  * { margin: 0; padding: 0; box-sizing: border-box; }
  html, body { width: 1200px; height: 900px; overflow: hidden; background: var(--paper); }
  body { position: relative; font-family: "Itim", "Sniglet", sans-serif; color: var(--ink); }

  .running-head { position: absolute; left: 12px; top: 28px; width: 1176px; height: 36px; background: var(--cocoa); }
  .running-head .tab { position: absolute; top: 0; height: 36px; background: var(--rust); color: #fff;
    font-size: 12px; line-height: 36px; }
  .running-head .tab-left { left: 0; width: 212px; padding-left: 14px; }
  .running-head .tab-right { right: 0; width: 210px; text-align: right; padding-right: 8px; }
  .running-head .folio { margin: 0 6px; }

  .photo { position: absolute; left: 12px; top: 64px; width: 588px; height: 796px;
    background: linear-gradient(160deg, #222a3a 0%, #161b27 60%, #1d2433 100%); }
  .photo .toast { position: absolute; border-radius: 38px 30px 24px 30px; }

  .recipe-page { position: absolute; left: 600px; top: 64px; width: 588px; height: 796px; }
  .day-title { position: absolute; left: 0; width: 586px; text-align: center; color: var(--rust);
    font-family: "Sniglet", "Itim", sans-serif; font-weight: 800; }
  .day-title.day { top: 24px; font-size: 28px; letter-spacing: 1px; }
  .day-title.theme { top: 60px; font-size: 31px; }
  .intro { position: absolute; left: 0; top: 107px; width: 586px; text-align: center;
    font-style: italic; font-size: 16.5px; line-height: 19.5px; }
  .diet-tags { position: absolute; left: 0; top: 182px; width: 586px; text-align: center; font-size: 16.5px; }

  .recipe { position: absolute; }
  .recipe h2 { font-family: "Sniglet", "Itim", sans-serif; font-weight: 800; font-size: 16.5px;
    color: var(--ink); line-height: 20px; text-transform: uppercase; }
  .recipe ul { list-style: none; font-size: 15.5px; line-height: 17.9px; }
  .recipe li::before { content: "• "; }
  .recipe li.wrap { padding-left: 10px; text-indent: -10px; }
  .link { text-decoration: underline; }

  .avocado-hummus { left: 58px; top: 228px; }
  .banana-cinnamon { left: 58px; top: 381px; }
  .pear-walnut { left: 265px; top: 535px; }
  .tropical-coconut { left: 265px; top: 652px; }

  .sketch { position: absolute; background: var(--sketch-bg); border-radius: 6px; }
</style>
</head>
<body>
  <header class="running-head">
    <div class="tab tab-left"><span class="folio">6</span> Morning Mission</div>
    <div class="tab tab-right">Morning Mission <span class="folio">7</span></div>
  </header>

  <div class="photo" role="img" aria-label="Overhead photo of four slices of sourdough toast on a dark slate board: coconut yoghurt with kiwifruit and strawberries, nut butter with banana, dates and pepitas, tahini with pear, walnuts and greens, and hummus with sliced avocado, hemp seeds and lemon">
    <div class="toast" style="left:48px;top:20px;width:232px;height:346px;background:linear-gradient(150deg,#e9e4dc,#b9b046 55%,#c64030);"></div>
    <div class="toast" style="left:324px;top:24px;width:226px;height:326px;background:linear-gradient(150deg,#f0e8d2,#ddd0b0 60%,#6b4a2f);"></div>
    <div class="toast" style="left:50px;top:424px;width:232px;height:344px;background:linear-gradient(150deg,#d8c9a4,#e6dcc0 50%,#5b6a34);"></div>
    <div class="toast" style="left:340px;top:420px;width:240px;height:356px;background:linear-gradient(150deg,#b4c46a,#7fae3a 55%,#d9d5be);"></div>
  </div>

  <main class="recipe-page">
    <h1 class="day-title day">TUESDAY</h1>
    <p class="day-title theme">Epic Toast Toppers</p>
    <p class="intro">Need some toast topping inspiration? Try a few of<br>the following combinations to step up<br>your morning toast game.</p>
    <p class="diet-tags">DF, Vegan, RSF, GF option</p>

    <section class="recipe avocado-hummus">
      <h2>Avocado Hummus :</h2>
      <ul>
        <li>1 slice fresh bread (GF if required)</li>
        <li><span class="link">Hummus</span> (make a batch of your own)</li>
        <li>Sliced avocado</li>
        <li>Hemp seeds</li>
        <li>Lemon juice</li>
        <li>Salt and pepper</li>
        <li>Snow pea sprouts</li>
      </ul>
    </section>
    <div class="sketch" style="left:330px;top:214px;width:160px;height:156px;" role="img" aria-label="Hand-drawn sketch of a halved avocado"></div>

    <section class="recipe banana-cinnamon">
      <h2>Banana Cinnamon :</h2>
      <ul>
        <li>1 slice fresh bread (GF if required)</li>
        <li class="wrap">Almond or <span class="link">peanut butter</span> (make a batch<br>of your own for the week)</li>
        <li>Sliced banana</li>
        <li>Chopped medjool dates</li>
        <li>Pepitas (pumpkin seeds)</li>
        <li>Cinnamon</li>
      </ul>
    </section>
    <div class="sketch" style="left:382px;top:386px;width:162px;height:126px;" role="img" aria-label="Hand-drawn sketch of a bunch of bananas"></div>

    <div class="sketch" style="left:86px;top:540px;width:110px;height:120px;" role="img" aria-label="Hand-drawn sketch of a pear"></div>
    <div class="sketch" style="left:96px;top:666px;width:96px;height:86px;" role="img" aria-label="Hand-drawn sketch of a halved kiwifruit"></div>

    <section class="recipe pear-walnut">
      <h2>Pear and Walnut :</h2>
      <ul>
        <li>1 slice fresh bread (GF if required)</li>
        <li>Tahini</li>
        <li>Sliced pear</li>
        <li>Chopped walnuts</li>
        <li>Drizzle of maple syrup</li>
      </ul>
    </section>

    <section class="recipe tropical-coconut">
      <h2>Tropical Coconut :</h2>
      <ul>
        <li>1 slice fresh bread (GF if required)</li>
        <li>Coconut yoghurt</li>
        <li>Fresh kiwifruit</li>
        <li>Fresh strawberries</li>
        <li>Sprinkle of desiccated coconut</li>
      </ul>
    </section>
  </main>
</body>
</html>
```